Tall Harbor Business Card

We are a Video Production and Video Equipment Rental company specialising in the supply of state of the art Video Technology and Services for the Live Entertainment, Television and Corporate Business Theatre markets. (in Sydney, Australia) www.tallharbor.example

Industry/Entity Type

Business

Contact Information for Business Card

name, position, email, website, address, logo
Example attached of the information we need - doesn't necessarily have to look the same

Font styles to use
Other font styles liked:
• Tall Harbor logo font is GOTHAM

Colors
ea1f27

Requirements
Nice to have
• either matt black or shiny black cards -
raised logo

```html
<!DOCTYPE html>
<html lang="en">
<head>
<meta charset="utf-8">
<title>Tall Harbor Business Card</title>
<link rel="stylesheet" href="https://fonts.googleapis.com/css2?family=Open+Sans:wght@400;600;700&display=swap">
<style>
  :root {
    --backdrop: #ececec;
    --card-black: #0c0c0d;
    --ink-white: #f2f2f2;
    --ink-soft: #c9c9c9;
    --brand-red: #ea1f27;
  }
  * { margin: 0; padding: 0; box-sizing: border-box; }
  html, body {
    width: 1200px; height: 675px; overflow: hidden;
    background: var(--backdrop);
    font-family: "Open Sans", Arial, sans-serif;
  }
  .stage {
    position: relative; width: 1200px; height: 675px;
    display: flex; align-items: center; justify-content: center; gap: 60px;
  }
  .card {
    position: relative; width: 520px; height: 297px;
    background: var(--card-black); color: var(--ink-white);
    box-shadow: 0 6px 18px rgba(0,0,0,0.18);
  }
  .card-front { display: flex; align-items: center; justify-content: center; }
  .wordmark {
    font-weight: 700; letter-spacing: 0.06em; text-transform: uppercase;
    color: var(--ink-white);
  }
  .card-front .wordmark { font-size: 44px; }
  .contact-person { position: absolute; left: 28px; top: 26px; }
  .person-name {
    color: var(--brand-red); font-size: 15px; font-weight: 600;
    text-transform: uppercase; line-height: 1.1;
  }
  .person-role {
    font-size: 10px; text-transform: uppercase; color: var(--ink-soft);
    letter-spacing: 0.02em;
  }
  .contact-online {
    position: absolute; right: 28px; top: 26px; text-align: right;
    font-size: 13px; text-transform: uppercase; line-height: 1.35;
  }
  .contact-online .web-highlight { color: var(--brand-red); }
  .address {
    position: absolute; left: 28px; top: 118px;
    font-size: 15px; text-transform: uppercase; line-height: 1.3;
  }
  .card-back .wordmark {
    position: absolute; right: 28px; top: 130px; font-size: 26px;
  }
  .services {
    position: absolute; left: 28px; right: 28px; bottom: 22px;
    font-size: 13.5px; text-transform: uppercase; letter-spacing: 0.02em;
    white-space: nowrap;
  }
</style>
</head>
<body>
  <main class="stage">
    <section class="card card-front" aria-label="Card front">
      <span class="wordmark">Tall Harbor</span>
    </section>

    <section class="card card-back" aria-label="Card back">
      <div class="contact-person">
        <p class="person-name">Dana Whitfield</p>
        <p class="person-role">Managing Director</p>
      </div>
      <div class="contact-online">
        <p>dana@tallharbor.example</p>
        <p>www.<span class="web-highlight">tallharbor</span>.example</p>
      </div>
      <address class="address" style="font-style:normal">
        12 Wharf Lane<br>
        Harbourside NSW 2000<br>
        Australia
      </address>
      <span class="wordmark">Tall Harbor</span>
      <p class="services">Video Solutions - LED Screens - Camera Systems - Projection</p>
    </section>
  </main>
</body>
</html>
```